MOVIE POSTER - THRILLER/SUSPENSE - FEATURE FILM

We need a "coming soon" poster. We prefer that the final file is delivered as a photoshop file or similar so we can edit cast/crew/etc. once that information is available. For now, it can just say COMING SOON.

TITLE OF THE MOVIE: Vanished Beyond Crestmoor
TAGLINE: Seeing the future can't save you.
We are open to creative ideas on a cool font.
STORYLINE: VANISHED BEYOND CRESTMOOR is a suspenseful story laced with mystery. A woman named Wrenna witnesses a crime and flees the scene, wrecking her car as she escapes. Days later at the hospital, Wrenna awakens from a coma but has no recollection of the events that put her there. However, she is having some very strange aftereffects.... when the doctors brought her back from the brink of death, she brought back a little something extra: She's having visions of her future kidnapping and murder! It's a race against the clock as Wrenna tries to figure out who she can trust and who is trying to kill her. The most important question of all is: Can she solve her own murder before it happens and save herself?

SIZE: 30" x 40" - 300dpi

Elements you can include (but are not required):
Handgun
blonde female (long hair), but don't show the face
darker hair male, but don't show the face
1970 Starvane (not a main component, but could be background) (black)
missing person flier

MOOD IDEAS:
mystery
thriller
suspense
bad guys/local thugs/mafia type/not dressed well though/more street type

I like the finish style which gives posters a slight unpolished look to it (so it's more like a drawing almost, and not a glossy photograph). Here are a couple examples of the finish that I am talking about:
http://www.reelsheetgallery.com/2015/hollow_ridge_ver4.html
http://www.reelsheetgallery.com/2015/copper_tide_ver5.html

Here was a rough mock-up I put together but by no means what we want. It was just to create a mood and feel.
http://brackenlamp.com/images/PosterVanishedBeyond.jpg

Here are a few posters that we like:
http://www.reelsheetgallery.com/2010/grey_orchard.html
http://www.reelsheetgallery.com/2001/iron_meadow_ver6.html
http://www.reelsheetgallery.com/2001/quiet_bastion_ver1.html
http://www.reelsheetgallery.com/2004/durnik_ver2.html
http://www.reelsheetgallery.com/2008/ferry_past_the_cold_shore.html
These are just a few ideas, but we are open to original ideas.

Please feel free to ask questions! We look forward to working with you.

Movie

• Information and examples are in the "project description."

```html
<!DOCTYPE html>
<html lang="en">
<head>
<meta charset="utf-8">
<title>Vanished Beyond Crestmoor — Coming Soon</title>
<link rel="stylesheet" href="https://fonts.googleapis.com/css2?family=Jost:wght@300;400;500&display=swap">
<style>
  :root {
    --stage: #ecebe8;
    --poster-top: #14b6f3;
    --poster-bottom: #0096e6;
    --ink: #111111;
    --paper: #ffffff;
    --figure-light: #8a8a8a;
    --figure-dark: #1c1c1c;
  }
  html, body {
    margin: 0;
    width: 1200px;
    height: 1148px;
    overflow: hidden;
    background: var(--stage);
  }
  .poster {
    position: absolute;
    left: 202px;
    top: 44px;
    width: 795px;
    height: 1060px;
    display: block;
  }
  .coming-soon {
    font-family: "Jost", sans-serif;
    font-weight: 300;
    font-size: 13px;
    letter-spacing: 22px;
    fill: var(--paper);
  }
  .tagline {
    font-family: "Jost", sans-serif;
    font-weight: 500;
    font-size: 17px;
    fill: var(--ink);
  }
  .title {
    font-family: "Jost", sans-serif;
    font-weight: 400;
    fill: var(--ink);
  }
  .title-small { font-size: 24px; }
  .title-large { font-size: 150px; }
  .title-fade { filter: url(#fade-blur); }
</style>
</head>
<body>
  <svg class="poster" viewBox="0 0 795 1060" xmlns="http://www.w3.org/2000/svg">
    <defs>
      <linearGradient id="poster-bg" x1="0" y1="0" x2="1" y2="1">
        <stop offset="0" stop-color="var(--poster-top)"/>
        <stop offset="1" stop-color="var(--poster-bottom)"/>
      </linearGradient>
      <linearGradient id="figure-tone" x1="0" y1="0" x2="0" y2="1">
        <stop offset="0" stop-color="var(--figure-light)"/>
        <stop offset="0.15" stop-color="var(--figure-dark)"/>
        <stop offset="0.45" stop-color="var(--figure-dark)"/>
        <stop offset="0.55" stop-color="#5d6064"/>
        <stop offset="1" stop-color="#2e3033"/>
      </linearGradient>
      <filter id="fade-blur" x="-10%" y="-30%" width="120%" height="160%">
        <feGaussianBlur stdDeviation="4"/>
      </filter>
    </defs>

    <rect class="poster-background" width="795" height="1060" fill="url(#poster-bg)"/>

    <text class="coming-soon" x="60" y="62">COMING SOON . . .</text>

    <rect class="heroine-figure" x="548" y="255" width="130" height="505" rx="40"
          fill="url(#figure-tone)" role="img"
          aria-label="Black and white photo of a blonde woman in a black leather jacket and jeans, seen from behind, holding a revolver"/>

    <text class="tagline" x="165" y="560" textLength="356" lengthAdjust="spacingAndGlyphs">SEEING THE FUTURE CAN'T SAVE YOU.</text>

    <text class="title title-small" x="88" y="712" textLength="150" lengthAdjust="spacingAndGlyphs">VANISHED</text>
    <text class="title title-large" x="248" y="712" textLength="492" lengthAdjust="spacingAndGlyphs">BEYOND</text>

    <text class="title title-large" x="220" y="868" textLength="292" lengthAdjust="spacingAndGlyphs">CREST</text>
    <text class="title title-large title-fade" x="522" y="868" textLength="220" lengthAdjust="spacingAndGlyphs">MOOR</text>
  </svg>
</body>
</html>
```